Business Card Design Project

we need a business card design for our company: www.dravonix.ch
It's important to include our already existing logo (see website)

```html
<!DOCTYPE html>
<html lang="de">
<head>
<meta charset="utf-8">
<title>Dravonix – Visitenkarte</title>
<link rel="stylesheet" href="https://fonts.googleapis.com/css2?family=Open+Sans:wght@400;600;700&display=swap">
<style>
  :root {
    --page-bg: #e9e7e3;
    --card-white: #ffffff;
    --brand-blue: #1f6298;
    --brand-blue-dark: #18507e;
    --brand-blue-light: #7ea6d6;
    --brand-logo: #2f6ea8;
    --back-logo: #7aa6d8;
    --text-dark: #2b2b2b;
    --text-muted: #3d3d3d;
  }
  * { box-sizing: border-box; margin: 0; padding: 0; }
  html, body {
    width: 1200px; height: 900px; overflow: hidden;
    background: var(--page-bg);
    font-family: "Open Sans", Arial, sans-serif;
  }
  .canvas { position: relative; width: 1200px; height: 900px; }

  .card {
    position: absolute; top: 292px;
    width: 552px; height: 314px;
    box-shadow: 0 2px 8px rgba(0,0,0,0.18);
    overflow: hidden;
  }
  .card--front { left: 30px; background: var(--card-white); }
  .card--back { left: 618px; background: var(--brand-blue); }

  .edge-stripe { position: absolute; left: 0; top: 0; width: 21px; height: 100%; }
  .edge-stripe__top { position: absolute; left: 0; top: 0; width: 100%; height: 98px; background: var(--brand-blue-light); }
  .edge-stripe__bottom { position: absolute; left: 0; top: 98px; width: 100%; bottom: 0; background: var(--brand-blue); }
  .card--back .edge-stripe__top { height: 108px; }
  .card--back .edge-stripe__bottom { top: 108px; background: var(--brand-blue-dark); }

  .contact { position: absolute; left: 45px; top: 66px; color: var(--text-dark); }
  .contact__name { font-size: 20px; font-weight: 700; color: var(--brand-blue); line-height: 1.1; }
  .contact__role { font-size: 14px; line-height: 1.2; color: var(--text-muted); }
  .contact__company { margin-top: 14px; font-size: 14px; font-weight: 700; line-height: 1.45; }
  .contact__address { font-size: 14px; line-height: 1.5; color: var(--text-muted); }
  .contact__lines { margin-top: 16px; list-style: none; }
  .contact__line { display: flex; align-items: center; font-size: 14px; line-height: 21px; color: var(--text-muted); }
  .contact__icon { width: 13px; height: 11px; margin-right: 9px; fill: var(--brand-blue); }

  .wordmark {
    position: absolute; font-weight: 600; letter-spacing: -0.5px; line-height: 1;
  }
  .card--front .wordmark { left: 252px; top: 128px; font-size: 50px; color: var(--brand-logo); }
  .card--back .wordmark { left: 140px; top: 128px; font-size: 50px; color: var(--back-logo); }
  .web-address {
    position: absolute; left: 142px; top: 182px;
    font-size: 15px; letter-spacing: 4px; color: var(--back-logo);
  }
</style>
</head>
<body>
<main class="canvas">
  <section class="card card--front" aria-label="Visitenkarte Vorderseite">
    <div class="edge-stripe"><div class="edge-stripe__top"></div><div class="edge-stripe__bottom"></div></div>
    <div class="contact">
      <p class="contact__name">Marco Keller</p>
      <p class="contact__role">President</p>
      <p class="contact__company">Dravonix AG</p>
      <p class="contact__address">Lindenhofstrasse 12<br>8005 Zürich</p>
      <ul class="contact__lines">
        <li class="contact__line">
          <svg class="contact__icon" viewBox="0 0 13 11" aria-hidden="true"><rect x="0" y="8" width="2.5" height="3"/><rect x="3.5" y="6" width="2.5" height="5"/><rect x="7" y="3.5" width="2.5" height="7.5"/><rect x="10.5" y="1" width="2.5" height="10"/></svg>
          0331 74 56789
        </li>
        <li class="contact__line">
          <svg class="contact__icon" viewBox="0 0 13 11" aria-hidden="true"><path d="M1 3.5C1 1.8 3.5 0.8 6.5 0.8S12 1.8 12 3.5v1H9.5V3.3H3.5v1.2H1z"/><path d="M2.5 5.5h8l1.5 5H1z"/></svg>
          044 610 33 44
        </li>
        <li class="contact__line">
          <svg class="contact__icon" viewBox="0 0 13 11" aria-hidden="true"><path d="M0.5 1h12v9h-12z M1.8 2.3v0.3l4.7 3.6 4.7-3.6v-0.3z M1.8 4.2v4.5h9.4V4.2l-4.7 3.5z" fill-rule="evenodd"/></svg>
          info@dravonix.ch
        </li>
      </ul>
    </div>
    <p class="wordmark">Dravonix</p>
  </section>

  <section class="card card--back" aria-label="Visitenkarte Rückseite">
    <div class="edge-stripe"><div class="edge-stripe__top"></div><div class="edge-stripe__bottom"></div></div>
    <p class="wordmark">Dravonix</p>
    <p class="web-address">www.dravonix.ch</p>
  </section>
</main>
</body>
</html>
```